Business card for Mortgage broker business

I have already had the logo designed and am needing a great looking business card. My business focus is on servicing clients who may not be able to obtain finance through traditional lenders due to bad credit, short term employment or they just don't fit the banks profile. It needs to be professional, trust worthy but also have a caring fell about it.
I have provided files showing the green and black logo, the white logo(on white background so the file looks blank) and also a file with the white logo with a background of leaves that was made up which will probably be used for a website header.

Industry/Entity Type

Finance

Contact Information for Business Card

Marcus Dalby
Managing Director, Accredited Finance Broker(AFB)
Po Box 817, Larkfield VIC 3964
marcus@kestrelfunding.com.au
www.kestrelfunding.com.au
0438 216 507

Requirements
Nice to have
• I have added a picture of myself as I would like to see some designs with the pic in it, but I'm not sure if I want it on there with the logo's or just the logo's

```html
<!DOCTYPE html>
<html lang="en">
<head>
<meta charset="utf-8">
<title>Kestrel Funding – Business Card</title>
<link rel="stylesheet" href="https://fonts.googleapis.com/css2?family=Open+Sans:wght@400;600;700&display=swap">
<style>
  :root {
    --page-bg: #f1f2f1;
    --brand-green: #0a6a37;
    --brand-green-dark: #05512a;
    --brand-green-light: #0f7a41;
    --card-white: #ffffff;
    --card-grey: #e9eaea;
    --swoosh-grey: #d9d9d9;
    --swoosh-highlight: #e6e6e6;
    --text-dark: #2a2a2a;
    --photo-top: #7f8a93;
    --photo-bottom: #2c3440;
  }
  * { box-sizing: border-box; margin: 0; padding: 0; }
  html, body {
    width: 1200px;
    height: 900px;
    overflow: hidden;
    background: var(--page-bg);
    font-family: "Open Sans", Arial, sans-serif;
  }
  .canvas {
    position: relative;
    width: 1200px;
    height: 900px;
  }
  .card {
    position: absolute;
    top: 302px;
    width: 520px;
    height: 297px;
    border-radius: 20px;
    overflow: hidden;
    box-shadow: 0 10px 24px rgba(0,0,0,0.18);
  }

  /* Front */
  .card-front {
    left: 50px;
    background: linear-gradient(135deg, var(--brand-green-light) 0%, var(--brand-green) 50%, var(--brand-green-dark) 100%);
    display: flex;
    align-items: center;
    justify-content: center;
  }
  .brand-name {
    font-weight: 600;
    letter-spacing: 0.04em;
    white-space: nowrap;
  }
  .card-front .brand-name {
    color: var(--card-white);
    font-size: 38px;
  }

  /* Back */
  .card-back {
    left: 630px;
    background: linear-gradient(160deg, var(--card-white) 0%, var(--card-grey) 100%);
  }
  .card-back .brand-name {
    position: absolute;
    left: 34px;
    top: 78px;
    color: var(--brand-green);
    font-size: 32px;
  }
  .holder {
    position: absolute;
    top: 22px;
    right: 26px;
    text-align: right;
  }
  .holder-name {
    color: var(--brand-green);
    font-size: 17px;
    font-weight: 700;
  }
  .holder-title {
    color: var(--text-dark);
    font-size: 10.5px;
    line-height: 1.4;
    margin-top: 2px;
  }
  .portrait {
    position: absolute;
    right: 26px;
    top: 108px;
    width: 92px;
    height: 110px;
    background: linear-gradient(180deg, var(--photo-top) 0%, var(--photo-bottom) 100%);
  }
  .swoosh {
    position: absolute;
    left: 0;
    bottom: 0;
    width: 520px;
    height: 80px;
  }
  .swoosh-grey { fill: var(--swoosh-grey); }
  .swoosh-green { fill: var(--brand-green); }
  .swoosh-white { fill: var(--card-white); }
  .swoosh-highlight { stroke: var(--swoosh-highlight); stroke-width: 4; fill: none; }
  .contact-list {
    position: absolute;
    left: 30px;
    top: 168px;
    list-style: none;
  }
  .contact-item {
    display: flex;
    align-items: center;
    gap: 6px;
    color: var(--text-dark);
    font-size: 13.5px;
    line-height: 20px;
    white-space: nowrap;
  }
  .contact-icon {
    width: 13px;
    height: 13px;
    fill: var(--brand-green);
    flex-shrink: 0;
  }
</style>
</head>
<body>
<main class="canvas">

  <section class="card card-front" aria-label="Business card front">
    <span class="brand-name">Kestrel Funding</span>
  </section>

  <section class="card card-back" aria-label="Business card back">
    <span class="brand-name">Kestrel Funding</span>

    <div class="holder">
      <div class="holder-name">Marcus Dalby</div>
      <div class="holder-title">Managing Director,<br>Accredited FINANCE Broker(AFB)</div>
    </div>

    <div class="portrait" role="img" aria-label="Portrait photo of Marcus Dalby in a dark suit"></div>

    <svg class="swoosh" viewBox="0 0 520 80" preserveAspectRatio="none" aria-hidden="true">
      <path class="swoosh-grey" d="M0 62 C120 44 260 74 380 40 C440 24 490 12 520 10 L520 80 L0 80 Z"/>
      <path class="swoosh-green" d="M0 66 C140 50 270 76 390 46 C450 32 495 20 520 18 L520 30 C490 34 450 46 395 58 C280 84 140 62 0 74 Z"/>
      <path class="swoosh-white" d="M0 74 C140 62 280 84 395 58 C450 46 490 34 520 30 L520 80 L0 80 Z"/>
      <path class="swoosh-highlight" d="M240 72 C330 66 420 42 520 24"/>
    </svg>

    <ul class="contact-list">
      <li class="contact-item">
        <svg class="contact-icon" viewBox="0 0 16 16" aria-hidden="true"><path d="M3.5 1 L6 1 L7 4.5 L5.3 5.8 C6.2 7.8 8.2 9.8 10.2 10.7 L11.5 9 L15 10 L15 12.5 C15 13.9 13.9 15 12.5 15 C6.7 15 1 9.3 1 3.5 C1 2.1 2.1 1 3.5 1 Z"/></svg>
        0438 216 507
      </li>
      <li class="contact-item">
        <svg class="contact-icon" viewBox="0 0 16 16" aria-hidden="true"><path d="M1 3 H15 V13 H1 Z M2 4 L8 9 L14 4 Z" fill-rule="evenodd"/></svg>
        marcus@kestrelfunding.com.au
      </li>
      <li class="contact-item">
        <svg class="contact-icon" viewBox="0 0 16 16" aria-hidden="true"><path d="M8 1 A7 7 0 1 0 8 15 A7 7 0 1 0 8 1 Z M8 2.5 C9 3.8 9.6 5.5 9.7 7.3 H6.3 C6.4 5.5 7 3.8 8 2.5 Z M6.3 8.7 H9.7 C9.6 10.5 9 12.2 8 13.5 C7 12.2 6.4 10.5 6.3 8.7 Z M2.6 7.3 C2.9 5.2 4.3 3.5 6.2 2.8 C5.4 4.1 5 5.7 4.9 7.3 Z M2.6 8.7 H4.9 C5 10.3 5.4 11.9 6.2 13.2 C4.3 12.5 2.9 10.8 2.6 8.7 Z M11.1 7.3 C11 5.7 10.6 4.1 9.8 2.8 C11.7 3.5 13.1 5.2 13.4 7.3 Z M11.1 8.7 H13.4 C13.1 10.8 11.7 12.5 9.8 13.2 C10.6 11.9 11 10.3 11.1 8.7 Z" fill-rule="evenodd"/></svg>
        www.kestrelfunding.com.au
      </li>
      <li class="contact-item">
        <svg class="contact-icon" viewBox="0 0 16 16" aria-hidden="true"><path d="M8 1 L15 7.5 H13 V15 H9.5 V10.5 H6.5 V15 H3 V7.5 H1 Z"/></svg>
        Po Box 817, Larkfield VIC 3964
      </li>
    </ul>
  </section>

</main>
</body>
</html>
```